High Tech Real Estate Startup needs a business card

We are developing an innovative real estate marketing product based around advanced search and virtual reality.

We talk to people, we need business cards.

Target Market(s)

The target market is technology professionals and realtors.

Contact Information for Business Card

The information to be included will include

Name
Title
Phone Number
E-mail Address
www.quelzo.com

It should use simple iconography for each one of those fields.

Font styles to use
Other font styles liked:
• Co, Jubilat, Avenir

Colors

Designer to choose colors to be used in the design.

Requirements
Must have
• Clean aesthetic,
• Good use of negative space.
• It should use our company logo, shown in the attached file. It is able to use the negative of that logo (coloured font and white background) and I have attached other acceptable accent colours in a swatch file.
Should not have
• Should not be too busy
• No extraneous text (slogans, tag lines etc)

```html
<!DOCTYPE html>
<html lang="en">
<head>
<meta charset="utf-8">
<title>Quelzo business card</title>
<link href="https://fonts.googleapis.com/css2?family=Roboto+Condensed:wght@400;700&display=swap" rel="stylesheet">
<style>
  :root {
    --teal: #18bfc4;
    --teal-deep: #0fb5ba;
    --white: #ffffff;
    --backdrop: #eceff0;
    --card-w: 540px;
    --card-h: 309px;
  }
  * { margin: 0; padding: 0; box-sizing: border-box; }
  html, body { width: 1200px; height: 911px; overflow: hidden; }
  body {
    background: var(--backdrop);
    font-family: "Roboto Condensed", Arial, sans-serif;
    display: flex;
    align-items: center;
    justify-content: center;
    gap: 40px;
  }
  .card {
    position: relative;
    width: var(--card-w);
    height: var(--card-h);
    background: var(--teal);
    color: var(--white);
    overflow: hidden;
    box-shadow: 0 6px 18px rgba(0,0,0,0.12);
  }
  .card--back { background: var(--teal-deep); }
  .wordmark {
    font-weight: 400;
    letter-spacing: 2px;
    color: var(--white);
    line-height: 1;
  }
  .card--front .wordmark {
    position: absolute;
    top: 58px;
    left: 218px;
    font-size: 50px;
  }
  .card--back .wordmark {
    position: absolute;
    inset: 0;
    display: flex;
    align-items: center;
    justify-content: center;
    font-size: 72px;
    letter-spacing: 4px;
  }
  .edge-band { position: absolute; left: 0; bottom: 0; }
  .site {
    position: absolute;
    left: 22px;
    bottom: 11px;
    font-size: 12px;
    letter-spacing: 4px;
    color: var(--teal);
  }
  .contact {
    position: absolute;
    left: 26px;
    bottom: 54px;
  }
  .contact__name { font-size: 19px; font-weight: 700; letter-spacing: 0.5px; }
  .contact__title { font-size: 12px; margin-bottom: 8px; opacity: 0.95; }
  .contact__row {
    display: flex;
    align-items: center;
    gap: 7px;
    font-size: 12px;
    line-height: 18px;
  }
  .contact__row svg { width: 11px; height: 11px; flex: none; }
</style>
</head>
<body>

  <section class="card card--front">
    <div class="wordmark">QUELZO</div>

    <div class="contact">
      <div class="contact__name">DANA WHITLOCK</div>
      <div class="contact__title">CEO/FOUNDER</div>
      <div class="contact__row">
        <svg viewBox="0 0 12 12" aria-hidden="true">
          <path d="M2.5 1 L4.5 1 L5.2 3.6 L3.9 4.6 Q5 7 7.4 8.1 L8.4 6.8 L11 7.5 L11 9.5 Q10.5 11 9 11 Q1 10.5 1 3 Q1 1.5 2.5 1 Z" fill="var(--white)"/>
        </svg>
        <span>555 210 4830</span>
      </div>
      <div class="contact__row">
        <svg viewBox="0 0 12 12" aria-hidden="true">
          <rect x="0.5" y="2" width="11" height="8" fill="var(--white)"/>
          <path d="M0.5 2.5 L6 6.5 L11.5 2.5" fill="none" stroke="var(--teal)" stroke-width="1"/>
        </svg>
        <span>dana@quelzo.com</span>
      </div>
    </div>

    <svg class="edge-band" width="540" height="60" viewBox="0 0 540 60" aria-hidden="true">
      <path d="M0 60 V24 H214 C230 24 234 46 250 46 H540 V60 Z" fill="var(--white)"/>
      <line x1="252" y1="40" x2="540" y2="40" stroke="var(--white)" stroke-width="2"/>
    </svg>
    <div class="site">WWW.QUELZO.COM</div>
  </section>

  <section class="card card--back">
    <div class="wordmark">QUELZO</div>
  </section>

</body>
</html>
```